need a profesional architect business card and logo

Hello everybody..i'm architect and interior designer..i want to redesign my business card..all i want is simple,elegant minimalist and look profesional..please check the attachment..be creative guys..any new ideas are welcome..good luck !!
added information : preferred colour is black,grey,dark grey
-please check new attachment
-i would like my company name change become dano welk architect and put some architect drawing in front page
-and i want the logo on the front page and other information on the back page

Good luck !

```html
<!DOCTYPE html>
<html lang="en">
<head>
<meta charset="utf-8">
<title>Dano Welk Architect – Business Card</title>
<link rel="stylesheet" href="https://fonts.googleapis.com/css2?family=Jost:wght@300&family=Libre+Baskerville&display=swap">
<style>
  :root {
    --sheet: #ffffff;
    --sheet-edge: #c8c8c8;
    --card: #ffffff;
    --ink: #111111;
    --name: #555555;
    --contact: #bdbdbd;
    --label: #9a9a9a;
    --shadow: rgba(0, 0, 0, 0.45);
  }
  * { margin: 0; padding: 0; box-sizing: border-box; }
  html, body { width: 1200px; height: 764px; overflow: hidden; background: var(--sheet); }
  .sheet {
    position: relative;
    width: 1200px; height: 764px;
    border: 1px solid var(--sheet-edge);
    background: var(--sheet);
    font-family: "Jost", sans-serif;
    font-weight: 300;
  }
  .card {
    position: absolute;
    width: 475px; height: 280px;
    background: var(--card);
    box-shadow: 7px 9px 10px var(--shadow);
    overflow: hidden;
  }
  .card--front   { left: 48px;  top: 51px; }
  .card--back    { left: 48px;  top: 377px; }
  .card--preview { left: 617px; top: 149px; }

  .preview-label {
    position: absolute;
    left: 617px; top: 124px;
    font-size: 10px;
    letter-spacing: 0.08em; text-transform: uppercase;
    color: var(--label);
  }

  .baseline {
    position: absolute;
    left: 0; top: 207px;
    height: 2px; background: var(--ink);
  }
  .card--front .baseline   { width: 405px; }
  .card--back .baseline    { width: 425px; }
  .card--preview .baseline { width: 423px; }

  .brand-name {
    position: absolute;
    font-size: 29px; line-height: 1;
    letter-spacing: 0.04em; color: var(--name);
    white-space: nowrap;
  }
  .card--front .brand-name   { right: 72px; top: 174px; }
  .card--preview .brand-name { right: 76px; top: 174px; }

  .brand-tagline {
    position: absolute;
    font-family: "Libre Baskerville", serif;
    font-size: 7px; color: var(--name);
    white-space: nowrap;
  }
  .card--front .brand-tagline   { right: 72px; top: 213px; }
  .card--preview .brand-tagline { right: 76px; top: 213px; }

  .contact {
    position: absolute;
    list-style: none;
    font-size: 12px; line-height: 25.3px;
    letter-spacing: 0.06em; text-transform: uppercase;
    color: var(--contact);
  }
  .card--back .contact    { left: 16px; top: 82px; }
  .card--preview .contact { left: 21px; top: 78px; }
</style>
</head>
<body>
<main class="sheet">

  <section class="card card--front" aria-label="Card front">
    <span class="brand-name">Dano Welk</span>
    <span class="baseline"></span>
    <span class="brand-tagline">Architecture &amp; Interior</span>
  </section>

  <section class="card card--back" aria-label="Card back">
    <ul class="contact">
      <li>2210 Alder Lane</li>
      <li>Hollis, WI 54620</li>
      <li>715-555-0142</li>
      <li>www.danowelk.com</li>
      <li>info@danowelk.com</li>
    </ul>
    <span class="baseline"></span>
  </section>

  <p class="preview-label">Transparent card preview</p>
  <section class="card card--preview" aria-label="Transparent card preview">
    <ul class="contact">
      <li>2210 Alder Lane</li>
      <li>Hollis, WI 54620</li>
      <li>715-555-0142</li>
      <li>www.danowelk.com</li>
      <li>info@danowelk.com</li>
    </ul>
    <span class="brand-name">Dano Welk</span>
    <span class="baseline"></span>
    <span class="brand-tagline">Architecture &amp; Interior</span>
  </section>

</main>
</body>
</html>
```